German Headhunter/ HR Consultancy needs Business Cards Design

We need a business Card Design for our Company in Stuttgart. We are specialized as Headhunter/ HR Consultancy in Placement of specialist and managers in permanent employment. Please refer to our business logo.

```html
<!DOCTYPE html>
<html lang="en">
<head>
<meta charset="UTF-8">
<title>Kernwerk Personalberatung – Business Card</title>
<link href="https://fonts.googleapis.com/css2?family=Karla:wght@400;500;700&display=swap" rel="stylesheet">
<style>
  :root {
    --bg: #2a2a2c;
    --brand-blue: #3a4fb8;
    --brand-blue-bright: #4560d6;
    --card-dark: #1b1b1d;
    --text-light: #ffffff;
    --text-muted: #b9b9bd;
    --band-grey: #8e8e93;
  }
  * { margin: 0; padding: 0; box-sizing: border-box; }
  html, body { width: 1200px; height: 874px; overflow: hidden; }
  body {
    background: var(--bg);
    font-family: "Karla", sans-serif;
    position: relative;
  }
  .card {
    position: absolute;
    width: 640px;
    height: 366px;
    border-radius: 22px;
    overflow: hidden;
  }
  /* Front */
  .card-front {
    left: 300px; top: 48px;
    background: var(--brand-blue);
    color: var(--text-light);
  }
  .front-brand {
    position: absolute;
    left: 0; right: 0; top: 110px;
    display: flex; align-items: center; justify-content: center; gap: 18px;
  }
  .brand-square {
    width: 46px; height: 46px;
    background: var(--text-light);
  }
  .brand-name {
    font-weight: 700;
    line-height: 1;
    text-transform: uppercase;
  }
  .front-brand .brand-name { font-size: 40px; letter-spacing: 1px; }
  .front-brand .brand-name span { display: block; font-size: 22px; letter-spacing: 2px; margin-top: 4px; }
  .tagline {
    position: absolute;
    left: 80px; right: 80px; top: 230px;
    text-align: center;
    font-size: 15px;
    line-height: 1.45;
  }
  /* Back */
  .card-back {
    left: 220px; top: 470px;
    background: var(--card-dark);
    color: var(--text-muted);
  }
  .back-brand {
    position: absolute;
    right: 50px; top: 50px;
    display: flex; align-items: center; gap: 14px;
    color: var(--brand-blue-bright);
  }
  .back-brand .brand-square { width: 36px; height: 36px; background: var(--brand-blue-bright); }
  .back-brand .brand-name { font-size: 30px; }
  .back-brand .brand-name span { display: block; font-size: 16px; letter-spacing: 1.5px; margin-top: 3px; color: var(--text-muted); }
  .person { position: absolute; left: 70px; top: 118px; }
  .person-name {
    color: var(--brand-blue-bright);
    font-weight: 700; font-size: 22px; letter-spacing: 1px;
    text-transform: uppercase;
  }
  .person-role { font-size: 15px; margin-top: 2px; }
  .contacts { position: absolute; left: 50px; top: 182px; list-style: none; }
  .contacts li {
    display: flex; align-items: center; gap: 12px;
    font-size: 15px; color: var(--text-light); height: 22px;
  }
  .contacts svg { width: 12px; height: 12px; fill: var(--text-muted); }
  .divider {
    position: absolute; left: 50px; right: 50px; top: 178px;
    height: 1px; background: var(--brand-blue-bright);
  }
  .address {
    position: absolute; right: 50px; top: 250px;
    text-align: right; font-size: 15px; line-height: 1.35; color: var(--text-light);
  }
  .address .company { padding-bottom: 4px; border-bottom: 1px solid var(--brand-blue-bright); margin-bottom: 4px; }
  .address .web { color: var(--brand-blue-bright); }
  .band-blue { position: absolute; left: 0; bottom: 0; width: 430px; height: 14px; background: var(--brand-blue); }
  .band-grey { position: absolute; left: 434px; right: 0; bottom: 0; height: 14px; background: var(--band-grey); }
</style>
</head>
<body>
  <section class="card card-front">
    <div class="front-brand">
      <div class="brand-square"></div>
      <div class="brand-name">Kernwerk<span>Personalberatung</span></div>
    </div>
    <p class="tagline">We are specialized as Headhunter/ HR Consultancy in Placement of specialist and managers in permanent employment.</p>
  </section>

  <section class="card card-back">
    <div class="back-brand">
      <div class="brand-square"></div>
      <div class="brand-name">Kernwerk<span>Personalberatung</span></div>
    </div>
    <div class="person">
      <div class="person-name">Martin Keller</div>
      <div class="person-role">Founder &amp; CEO</div>
    </div>
    <div class="divider"></div>
    <ul class="contacts">
      <li><svg viewBox="0 0 12 12"><path d="M2.5 0.5l2 2-1 1.5c.6 1.5 1.9 2.8 3.5 3.5l1.5-1 2 2-1.5 2C4.5 11.5.5 7.5.5 2z"/></svg>936-512-7781</li>
      <li><svg viewBox="0 0 12 12"><rect x="3" y="0" width="6" height="12" rx="1"/></svg>936-274-9062</li>
      <li><svg viewBox="0 0 12 12"><rect x="0" y="4" width="12" height="6" rx="1"/><rect x="3" y="0" width="6" height="4"/></svg>936-358-1420</li>
      <li><svg viewBox="0 0 12 12"><rect x="0" y="2" width="12" height="8" rx="1"/></svg>martin@kernwerk.com</li>
    </ul>
    <div class="address">
      <div class="company">Kernwerk Personalberatung</div>
      <div>4120 Birch Hollow Road</div>
      <div>Juneau, Alaska 34890</div>
      <div class="web">www.kernwerk.com</div>
    </div>
    <div class="band-blue"></div>
    <div class="band-grey"></div>
  </section>
</body>
</html>
```